Redesign of existing business card

I would like the "signage" attachment converted into a business card. This needs to be double sided aswell, keeping the phone number and names on the front, and the email + website on the back.

Second attachment is the current business card design.

Larger font for contact details is required.

Must keep to original color themes (electric blue, silver/grey etc)

Back of the card to have blue background with white writing.

Industry/Entity Type

Business

Contact Information for Business Card

Refer to existing design from attachments

Requirements
Must have
• Refer to existing design from attachments
Nice to have

```html
<!DOCTYPE html>
<html lang="en">
<head>
<meta charset="utf-8">
<title>Voltara Electro Services – Business Card</title>
<link rel="stylesheet" href="https://fonts.googleapis.com/css2?family=Arimo:wght@400;700&display=swap">
<style>
  :root {
    --electric-blue: #2e4fa6;
    --electric-blue-deep: #223d8a;
    --silver: #c9cbcf;
    --silver-light: #eeeff1;
    --graphite: #2b2b2d;
    --charcoal: #3a3a3c;
    --paper: #f4f4f5;
    --stage: #e4e4e6;
    --white: #ffffff;
  }
  * { box-sizing: border-box; margin: 0; padding: 0; }
  html, body {
    width: 1200px; height: 1000px; overflow: hidden;
    background: var(--stage);
    font-family: "Arimo", Arial, sans-serif;
  }
  .card {
    position: absolute; left: 250px;
    width: 700px; height: 400px;
    overflow: hidden;
    box-shadow: 0 6px 18px rgba(0,0,0,0.18);
  }
  /* FRONT */
  .card--front { top: 50px; background: var(--paper); }
  .front__pattern {
    position: absolute; left: 0; top: 150px; width: 700px; height: 250px;
    background: linear-gradient(160deg, var(--silver-light) 0%, var(--silver) 55%, #a9b4d6 100%);
    opacity: 0.8;
  }
  .front__brand {
    position: absolute; left: 40px; top: 26px;
    color: var(--graphite); font-weight: 700;
    text-transform: uppercase; line-height: 1;
  }
  .front__brand-main { display: block; font-size: 104px; letter-spacing: 6px; }
  .front__brand-sub { display: block; font-size: 34px; letter-spacing: 4px; margin-top: 8px; }
  .front__bands { position: absolute; left: 0; top: 0; }
  .band-text {
    position: absolute; left: 28px; color: var(--white); font-weight: 700;
  }
  .band-text--name { top: 203px; font-size: 30px; }
  .band-text--phone { top: 262px; left: 84px; font-size: 48px; letter-spacing: 1px; }
  .band-text--licence { top: 340px; font-size: 22px; letter-spacing: 5px; font-weight: 400; }
  .phone-icon { position: absolute; left: 28px; top: 266px; }

  /* BACK */
  .card--back { top: 530px; background: var(--electric-blue); }
  .back__pattern {
    position: absolute; inset: 0;
    background: radial-gradient(circle at 68% 62%, rgba(34,61,138,0.85) 0%, rgba(46,79,166,0) 60%);
  }
  .back__contacts {
    position: absolute; left: 150px; top: 130px;
    list-style: none; color: var(--white);
  }
  .contact-line {
    display: flex; align-items: center; gap: 18px;
    font-size: 30px; font-weight: 700; margin-bottom: 34px;
  }
  .contact-line svg { flex: none; }
</style>
</head>
<body>

<section class="card card--front" aria-label="Business card front">
  <div class="front__pattern" role="img" aria-label="Faint circuit board pattern background"></div>

  <div class="front__brand">
    <span class="front__brand-main">Voltara</span>
    <span class="front__brand-sub">Electro Services</span>
  </div>

  <svg class="front__bands" width="700" height="400" viewBox="0 0 700 400" aria-hidden="true">
    <polygon points="0,196 400,196 420,244 0,244" fill="var(--charcoal)"/>
    <polygon points="0,250 445,250 470,322 0,322" fill="var(--electric-blue)"/>
    <polygon points="0,328 350,328 365,372 0,372" fill="var(--graphite)"/>
    <line x1="0" y1="247" x2="430" y2="247" stroke="var(--white)" stroke-width="2"/>
    <line x1="0" y1="325" x2="475" y2="325" stroke="var(--white)" stroke-width="2"/>
  </svg>

  <p class="band-text band-text--name">Daniel Voss</p>

  <svg class="phone-icon" width="44" height="44" viewBox="0 0 24 24" aria-hidden="true">
    <path fill="#fff" d="M6.6 10.8a15.1 15.1 0 0 0 6.6 6.6l2.2-2.2a1 1 0 0 1 1-.25 11.4 11.4 0 0 0 3.6.57 1 1 0 0 1 1 1V20a1 1 0 0 1-1 1A17 17 0 0 1 3 4a1 1 0 0 1 1-1h3.5a1 1 0 0 1 1 1c0 1.25.2 2.45.57 3.57a1 1 0 0 1-.25 1z"/>
  </svg>
  <p class="band-text band-text--phone">0400 555 123</p>

  <p class="band-text band-text--licence">EC24690</p>
</section>

<section class="card card--back" aria-label="Business card back">
  <div class="back__pattern" role="img" aria-label="Subtle circuit pattern over blue background"></div>
  <ul class="back__contacts">
    <li class="contact-line">
      <svg width="36" height="36" viewBox="0 0 24 24" aria-hidden="true">
        <circle cx="12" cy="12" r="11" fill="none" stroke="#fff" stroke-width="1.6"/>
        <rect x="5.5" y="7.5" width="13" height="9" fill="none" stroke="#fff" stroke-width="1.4"/>
        <polyline points="5.5,7.5 12,12.5 18.5,7.5" fill="none" stroke="#fff" stroke-width="1.4"/>
      </svg>
      <span>daniel@voltaraelectro.com</span>
    </li>
    <li class="contact-line">
      <svg width="36" height="36" viewBox="0 0 24 24" aria-hidden="true">
        <circle cx="12" cy="12" r="11" fill="none" stroke="#fff" stroke-width="1.6"/>
        <ellipse cx="12" cy="12" rx="4.5" ry="11" fill="none" stroke="#fff" stroke-width="1.3"/>
        <line x1="1" y1="12" x2="23" y2="12" stroke="#fff" stroke-width="1.3"/>
        <line x1="3" y1="6.5" x2="21" y2="6.5" stroke="#fff" stroke-width="1.1"/>
        <line x1="3" y1="17.5" x2="21" y2="17.5" stroke="#fff" stroke-width="1.1"/>
      </svg>
      <span>www.voltaraelectro.com.au</span>
    </li>
  </ul>
</section>

</body>
</html>
```